Asphalt Driveway Billboard Design

We need a billboard designed for an Asphalt & Concrete Company in Minnesota. We want to advertise Asphalt Driveways on this billboard! Logo is uploaded below. Our website is tamlin-paving.com for more information.

```html
<!DOCTYPE html>
<html lang="en">
<head>
<meta charset="utf-8">
<title>Tamlin Asphalt &amp; Concrete — Billboard</title>
<link href="https://fonts.googleapis.com/css2?family=Montserrat:wght@600;700;800&display=swap" rel="stylesheet">
<style>
  :root {
    --blue-deep: #0d56a3;
    --blue-mid: #1670bb;
    --blue-bright: #2395d3;
    --ink: #0a0a0a;
    --white: #ffffff;
    --strip: #ececec;
    --link-blue: #1a56a8;
    --badge-green: #6a9a3a;
    --badge-gold: #c9a83a;
    --partner-red: #d2453c;
    --partner-navy: #23507f;
    --partner-grey: #9aa3ad;
    --partner-orange: #e9893a;
    --page: #f7f5f5;
  }
  * { margin: 0; padding: 0; box-sizing: border-box; }
  html, body {
    width: 1050px; height: 1200px; overflow: hidden;
    background: var(--page);
    font-family: "Montserrat", Arial, sans-serif;
  }
  .billboard {
    position: absolute; left: 25px; top: 350px;
    width: 1000px; height: 500px; overflow: hidden;
    box-shadow: 4px 6px 10px rgba(0,0,0,.35);
  }
  .billboard__art { position: absolute; inset: 0; }
  .brand {
    position: absolute; left: 38px; top: 72px; width: 176px;
    text-align: center; color: var(--white);
  }
  .brand__mark {
    display: block; width: 34px; height: 34px; margin: 0 auto 8px;
    background: var(--white);
  }
  .brand__name { font-size: 31px; font-weight: 700; letter-spacing: 1px; line-height: 1; }
  .brand__tagline { font-size: 10.5px; font-weight: 600; letter-spacing: 1px; margin-top: 5px; white-space: nowrap; }
  .headline {
    position: absolute; left: 232px; width: 710px; top: 26px;
    text-align: center; color: var(--white);
    font-weight: 700; font-size: 51px; line-height: 56px;
    text-shadow: 2px 3px 4px rgba(0,0,0,.35);
    white-space: nowrap;
  }
  .phone {
    position: absolute; left: 272px; top: 146px;
    color: var(--white); font-weight: 800;
    text-shadow: 2px 3px 4px rgba(0,0,0,.35); white-space: nowrap;
  }
  .phone__label { font-size: 33px; font-weight: 700; }
  .phone__number { font-size: 55px; letter-spacing: 1px; }
  .license {
    position: absolute; left: 755px; top: 155px; width: 245px; height: 46px;
    background: var(--blue-deep); color: var(--white);
    text-align: right; padding: 6px 8px 0 0; font-weight: 700;
  }
  .license__title { font-size: 11px; line-height: 14px; }
  .license__number { font-size: 17px; line-height: 22px; }
  .credentials {
    position: absolute; left: 0; top: 446px; width: 1000px; height: 36px;
    background: var(--strip);
    display: flex; align-items: center; padding-left: 24px; gap: 18px;
  }
  .credentials__badges { display: flex; }
  .credentials__badges span {
    width: 28px; height: 28px; border-radius: 50%; margin-right: -6px;
    border: 2px solid var(--white);
  }
  .badge--green { background: var(--badge-green); }
  .badge--gold { background: var(--badge-gold); }
  .partner { height: 24px; border-radius: 3px; }
  .partner--red { width: 42px; background: var(--partner-red); }
  .partner--grey { width: 60px; background: var(--partner-grey); }
  .partner--navy { width: 86px; background: var(--partner-navy); }
  .partner--silver { width: 106px; background: var(--partner-grey); }
  .partner--orange { width: 106px; background: var(--partner-orange); }
  .contact {
    position: absolute; left: 732px; top: 446px;
    color: var(--link-blue); font-weight: 700; font-size: 14.5px; line-height: 17px;
    padding-top: 1px;
  }
</style>
</head>
<body>
  <section class="billboard">
    <svg class="billboard__art" viewBox="0 0 1000 500" width="1000" height="500" aria-hidden="false">
      <defs>
        <radialGradient id="panelBlue" cx="0.55" cy="0.35" r="0.6">
          <stop offset="0" stop-color="#2aa0da"/>
          <stop offset="0.55" stop-color="#1670bb"/>
          <stop offset="1" stop-color="#0d56a3"/>
        </radialGradient>
        <linearGradient id="photoTones" x1="0" y1="0" x2="0" y2="1">
          <stop offset="0" stop-color="#b9a88f"/>
          <stop offset="0.35" stop-color="#6d8a4a"/>
          <stop offset="0.6" stop-color="#3a3d40"/>
          <stop offset="1" stop-color="#4f8a2c"/>
        </linearGradient>
      </defs>
      <rect class="photo" x="0" y="180" width="1000" height="320" fill="url(#photoTones)" role="img" aria-label="Photo of a suburban home with a freshly sealed black asphalt driveway and green lawn"/>
      <path class="arc-shadow" d="M0,0 H1000 V336 Q527,92 0,378 Z" fill="var(--ink)"/>
      <path class="arc-panel" d="M0,0 H1000 V318 Q527,70 0,346 Z" fill="url(#panelBlue)"/>
    </svg>

    <div class="brand">
      <span class="brand__mark"></span>
      <div class="brand__name">TAMLIN</div>
      <div class="brand__tagline">— ASPHALT &amp; CONCRETE —</div>
    </div>

    <h1 class="headline">PREMIER ASPHALT &amp;<br>CONCRETE CONTRACTOR</h1>

    <p class="phone"><span class="phone__label">Tel: </span><span class="phone__number">763-555-0148</span></p>

    <div class="license">
      <div class="license__title">RESIDENTIAL BLDG CONTRACTOR LIC.</div>
      <div class="license__number">#BC512049.</div>
    </div>

    <div class="credentials">
      <div class="credentials__badges">
        <span class="badge--green"></span><span class="badge--gold"></span><span class="badge--green"></span><span class="badge--gold"></span><span class="badge--green"></span><span class="badge--gold"></span>
      </div>
      <span class="partner partner--red"></span>
      <span class="partner partner--grey"></span>
      <span class="partner partner--navy"></span>
      <span class="partner partner--silver"></span>
      <span class="partner partner--orange"></span>
    </div>

    <div class="contact">
      <div>sales@tamlin-paving.com</div>
      <div>tamlin-paving.com</div>
    </div>
  </section>
</body>
</html>
```